Etiketten für Saft-Range
grupotrinka suchte ein neues Design in der Kategorie Etiketten und hat ein Projekt auf grafikwerkstube.de gestartet.
Zielgruppe
Wir sind Getränkehersteller- und -händler. Für unsere Partner haben wir exklusive Eigenmarken, die nur unserer Partner verkaufen. Die veski Saft-Range ist eine exklusive Gastronomiemarke, die nicht im Handel erhältlich ist.
Aufgabenstellung
Das Layout unsere Eigenmarke veski soll in der Saft-Range einen Relaunch erhalten. Das ganze Sortiment besteht aktuell aus 10 Sorten. Es handelt sich um Glasflaschenetiketten, neue Stanzen beigefügt (Frontbauchetikett, Fronthalsetikett, Rückseitenetikett). Im ersten Schritt möchten wir nur die Sorten Kirsche & Apfel naturtrüb designen lassen.
Die Stanzen finden Sie beigefügt, sowie die aktuellen Layouts und Produktabbildungen der beiden genannten Sorten.
Zur Info, unsere Marke veski besteht ebenfalls aus einer Wasser-Range und Bittergetränke-Range. Die Abbildungen finden Sie zur Info ebenfalls anbei.
Folgende Bestandteile müssen auf die Etiketten (Materialfarbe weiß):
Front Bauchetikett:
- ob die Frucht als Foto oder als Zeichnung abgebildet wird ist uns erst einmal
- Marke veski
- Sorte
- Sortenzusatz wie z.B. Direktsaft
- Fruchtgehalt
- 1 l Pfandfalsche
- e - Zeichen
Rückseite:
- Marle veski
- Sortenzusatz s.o.
-Verkehrsbezeichnung
- Zutaten
- Nährwerttabelle je 100ml
- Lagerungshinweis
- 1l Pfandflasche
- Inverkehrbringeradresse
- Mindestens haltbar bis
ggf. eine Sortendifferenzierung über die Farben.
Die Glasflaschen sind klar.

```html
<!DOCTYPE html>
<html lang="de">
<head>
<meta charset="utf-8">
<title>veski Saft-Range – Etiketten</title>
<link rel="stylesheet" href="https://fonts.googleapis.com/css2?family=Arimo:wght@700&family=Barlow:wght@300;400;600&display=swap">
<style>
  :root {
    --paper: #ffffff;
    --apple-base: #bdd005;
    --apple-mid: #dcdc00;
    --apple-flesh: #fcf05e;
    --cherry-base: #cb192c;
    --cherry-bright: #e2001a;
    --cherry-dark: #b51826;
    --ink: #ffffff;
  }
  html, body {
    margin: 0;
    padding: 0;
    overflow: hidden;
    background: var(--paper);
  }
  .sheet {
    position: relative;
    width: 1153px;
    height: 1200px;
    overflow: hidden;
    background: var(--paper);
  }
  .neck-labels {
    position: absolute;
    left: 0;
    top: 0;
  }
  .neck-brand {
    font-family: "Barlow", sans-serif;
    font-weight: 300;
    font-size: 56px;
    fill: var(--ink);
  }
  .neck-variety {
    font-family: "Barlow", sans-serif;
    font-weight: 600;
    font-size: 15px;
    fill: var(--ink);
  }
  .body-label {
    position: absolute;
    top: 609px;
    width: 402px;
    height: 443px;
    overflow: hidden;
    color: var(--ink);
  }
  .body-label--apple { left: 101px; background: var(--apple-base); }
  .body-label--cherry { left: 634px; background: var(--cherry-base); }
  .fruit-art {
    position: absolute;
    inset: 0;
  }
  .body-label--apple .fruit-art {
    background:
      radial-gradient(ellipse 110px 120px at 60px 480px, var(--apple-flesh) 0 98%, transparent 100%),
      radial-gradient(ellipse 120px 130px at 95px 360px, var(--apple-mid) 0 98%, transparent 100%),
      radial-gradient(ellipse 115px 115px at 85px 110px, var(--apple-mid) 0 98%, transparent 100%),
      radial-gradient(ellipse 120px 135px at 330px 265px, var(--apple-mid) 0 98%, transparent 100%);
  }
  .body-label--cherry .fruit-art {
    background:
      radial-gradient(ellipse 115px 125px at 115px 115px, var(--cherry-bright) 0 98%, transparent 100%),
      radial-gradient(ellipse 110px 125px at 80px 325px, var(--cherry-bright) 0 98%, transparent 100%),
      radial-gradient(ellipse 105px 125px at 345px 295px, var(--cherry-dark) 0 98%, transparent 100%);
  }
  .brand {
    position: absolute;
    top: 14px;
    left: 0;
    right: 0;
    text-align: center;
    font-family: "Barlow", sans-serif;
    font-weight: 300;
    font-size: 56px;
    line-height: 1;
  }
  .variety {
    position: absolute;
    margin: 0;
    font-family: "Arimo", sans-serif;
    font-weight: 700;
    line-height: 1;
    letter-spacing: -2px;
    white-space: nowrap;
  }
  .body-label--apple .variety { left: -6px; top: 70px; font-size: 160px; }
  .body-label--cherry .variety { left: -24px; top: 95px; font-size: 132px; }
  .variety-suffix {
    position: absolute;
    right: -10px;
    top: 207px;
    font-family: "Arimo", sans-serif;
    font-weight: 700;
    font-size: 86px;
    line-height: 1;
    letter-spacing: -1px;
  }
  .variety-extra {
    position: absolute;
    left: 272px;
    top: 272px;
    font-family: "Barlow", sans-serif;
    font-weight: 400;
    font-size: 36px;
    line-height: 1;
    white-space: nowrap;
  }
  .fruit-content {
    position: absolute;
    right: 10px;
    top: 352px;
    margin: 0;
    text-align: right;
    font-family: "Barlow", sans-serif;
    font-weight: 600;
    font-size: 15px;
    line-height: 18px;
  }
  .volume {
    position: absolute;
    right: 10px;
    top: 400px;
    font-family: "Barlow", sans-serif;
    font-weight: 300;
    font-size: 25px;
    line-height: 1;
  }
  .deposit {
    position: absolute;
    right: 11px;
    top: 425px;
    font-family: "Barlow", sans-serif;
    font-weight: 400;
    font-size: 9.5px;
    line-height: 1;
  }
</style>
</head>
<body>
<main class="sheet">

  <svg class="neck-labels" width="1153" height="500" viewBox="0 0 1153 500">
    <g class="neck-label neck-label--apple">
      <path d="M201 160 Q302 174 403 160 L462 439 Q302 473 142 439 Z" fill="var(--apple-base)"/>
      <text class="neck-brand" x="303" y="228" text-anchor="middle">veski</text>
      <ellipse role="img" aria-label="Halbierter Apfel mit Kerngehäuse" cx="302" cy="330" rx="92" ry="82" fill="var(--apple-flesh)" stroke="var(--apple-mid)" stroke-width="10"/>
      <text class="neck-variety" x="302" y="436" text-anchor="middle">Apfelsaft naturtrüb</text>
    </g>
    <g class="neck-label neck-label--cherry">
      <path d="M734 160 Q835 174 936 160 L995 439 Q835 473 675 439 Z" fill="var(--cherry-base)"/>
      <text class="neck-brand" x="836" y="228" text-anchor="middle">veski</text>
      <rect role="img" aria-label="Zwei Kirschen am Stiel" x="764" y="244" width="146" height="153" rx="40" fill="var(--cherry-bright)"/>
      <text class="neck-variety" x="840" y="436" text-anchor="middle">Kirschsaft</text>
    </g>
  </svg>

  <section class="body-label body-label--apple">
    <div class="fruit-art" role="img" aria-label="Große Apfelhälften in Grün- und Gelbtönen"></div>
    <div class="brand">veski</div>
    <h2 class="variety">Apfel</h2>
    <div class="variety-suffix">saft</div>
    <div class="variety-extra">naturtrüb</div>
    <p class="fruit-content">Fruchtgehalt:<br>min. 50%</p>
    <div class="volume">℮ 1,0 l</div>
    <div class="deposit">PFANDFLASCHE</div>
  </section>

  <section class="body-label body-label--cherry">
    <div class="fruit-art" role="img" aria-label="Große Kirschen in Rottönen"></div>
    <div class="brand">veski</div>
    <h2 class="variety">Kirsch</h2>
    <div class="variety-suffix">saft</div>
    <p class="fruit-content">Fruchtgehalt:<br>min. 50%</p>
    <div class="volume">℮ 1,0 l</div>
    <div class="deposit">PFANDFLASCHE</div>
  </section>

</main>
</body>
</html>
```